We need a business card design for Corvana Group. We are a healthcare recruiting, wellness and education company. We partner with medical facilities to find quality candidates. We also offer free wellness courses.
The final design should communicate an emphasis on recruiting and wellness
The main purpose of the business card is to utilized it for networking events, give to hospitals, executives, VCs surgery centers and clinics. I want it to be sleek, clean, use of our brand colors and professional.

```html
<!DOCTYPE html>
<html lang="en">
<head>
<meta charset="utf-8">
<title>Corvana Group – Business Card</title>
<link rel="stylesheet" href="https://fonts.googleapis.com/css2?family=Montserrat:wght@400;600;800&family=Questrial&display=swap">
<style>
  :root {
    --backdrop: #3e5457;
    --card: #f3fcfb;
    --teal-deep: #065c52;
    --teal-bright: #2cbfa4;
    --ink: #0a5a50;
    --ink-soft: #3f6f69;
  }
  * { margin: 0; padding: 0; box-sizing: border-box; }
  html, body { width: 1200px; height: 1200px; overflow: hidden; }
  body {
    background: var(--backdrop);
    display: flex; flex-direction: column; align-items: center; justify-content: center;
    gap: 60px;
    font-family: "Questrial", sans-serif;
  }
  .card {
    position: relative; width: 840px; height: 480px;
    background: var(--card); border-radius: 14px; overflow: hidden;
    box-shadow: 0 18px 40px rgba(0,0,0,.35);
  }
  .card__wave { position: absolute; inset: 0; width: 100%; height: 100%; }
  .brand { position: absolute; display: flex; align-items: center; gap: 22px; color: var(--ink); }
  .brand__square { width: 70px; height: 70px; background: var(--ink); border-radius: 6px; }
  .brand__name { font-family: "Questrial", sans-serif; line-height: .95; }
  .brand__primary { display: block; font-size: 78px; }
  .brand__secondary { display: block; font-size: 40px; text-align: right; }
  .card--front .brand { left: 200px; top: 140px; }
  .card--back .brand { right: 80px; top: 50px; gap: 16px; }
  .card--back .brand__square { width: 48px; height: 48px; }
  .card--back .brand__primary { font-size: 54px; }
  .card--back .brand__secondary { font-size: 28px; }
  .contact { position: absolute; left: 60px; top: 210px; color: var(--ink); }
  .contact__name { font-family: "Montserrat", sans-serif; font-weight: 800; font-size: 28px; letter-spacing: .5px; }
  .contact__role { font-family: "Montserrat", sans-serif; font-weight: 400; font-size: 14px; letter-spacing: 8px; color: var(--ink-soft); margin-top: 2px; padding-bottom: 8px; border-bottom: 1.5px solid var(--ink); width: 330px; }
  .contact__address { font-size: 14px; margin-top: 8px; color: var(--ink-soft); }
  .contact__list { list-style: none; margin-top: 60px; }
  .contact__item { display: flex; align-items: center; gap: 10px; font-size: 16px; color: var(--ink-soft); margin-bottom: 8px; }
  .contact__icon { width: 16px; height: 16px; flex: none; }
</style>
</head>
<body>

<section class="card card--front" aria-label="Business card front">
  <svg class="card__wave" viewBox="0 0 840 480" preserveAspectRatio="none" aria-hidden="true">
    <path d="M150 480 C 420 440, 560 300, 840 180 L 840 480 Z" fill="var(--teal-bright)"/>
    <path d="M190 480 C 440 450, 580 320, 840 200 L 840 480 Z" fill="var(--card)"/>
    <path d="M220 480 C 460 460, 600 340, 840 220 L 840 480 Z" fill="var(--teal-deep)"/>
  </svg>
  <div class="brand">
    <span class="brand__square"></span>
    <span class="brand__name"><span class="brand__primary">Corvana</span><span class="brand__secondary">Group</span></span>
  </div>
</section>

<section class="card card--back" aria-label="Business card back">
  <svg class="card__wave" viewBox="0 0 840 480" preserveAspectRatio="none" aria-hidden="true">
    <path d="M480 480 C 640 400, 720 260, 840 130 L 840 480 Z" fill="var(--teal-bright)"/>
    <path d="M500 480 C 660 410, 740 280, 840 150 L 840 480 Z" fill="var(--card)"/>
    <path d="M525 480 C 680 420, 760 300, 840 170 L 840 480 Z" fill="var(--teal-deep)"/>
  </svg>
  <div class="brand">
    <span class="brand__square"></span>
    <span class="brand__name"><span class="brand__primary">Corvana</span><span class="brand__secondary">Group</span></span>
  </div>
  <div class="contact">
    <h1 class="contact__name">Marcus T. Elling</h1>
    <p class="contact__role">GENERAL MANAGER</p>
    <p class="contact__address">88 Harbor Lane, Lakeview, CA 90210</p>
    <ul class="contact__list">
      <li class="contact__item">
        <svg class="contact__icon" viewBox="0 0 16 16" aria-hidden="true"><path d="M4 1.5 6 4 4.8 5.8c.8 1.9 2.3 3.4 4.2 4.2L10.8 8.8 13.5 10.5 12.5 13.5C7 13.5 2.5 9 2.5 3.5Z" fill="none" stroke="currentColor" stroke-width="1.3"/></svg>
        555-204-7781
      </li>
      <li class="contact__item">
        <svg class="contact__icon" viewBox="0 0 16 16" aria-hidden="true"><circle cx="8" cy="8" r="6.5" fill="none" stroke="currentColor" stroke-width="1.3"/><path d="M1.5 8h13M8 1.5c-3 3.5-3 9.5 0 13M8 1.5c3 3.5 3 9.5 0 13" fill="none" stroke="currentColor" stroke-width="1.1"/></svg>
        www.corvanagroup.com
      </li>
      <li class="contact__item">
        <svg class="contact__icon" viewBox="0 0 16 16" aria-hidden="true"><rect x="1.5" y="3.5" width="13" height="9" fill="none" stroke="currentColor" stroke-width="1.3"/><path d="M1.5 3.5 8 9l6.5-5.5" fill="none" stroke="currentColor" stroke-width="1.3"/></svg>
        info@corvanagroup.com
      </li>
    </ul>
  </div>
</section>

</body>
</html>
```